HARD MONEY ORIGINATOR RECRUITMENT.
Looking for individuals to help us originate loans for real estate investor financing primarily used to fix up properties and resell.
HARD MONEY ORIGINATORS WANTED
No Licensing Required
Work As Independent Contractor
1% Flat Finders Fee on Each Loan
Referral Compensation for Recruiting New Originators
Immediate Payouts
Programs Offered Nationwide
Marketing Assistance and Support Available
Email mpelton@brightquaylending.com for more information or call (800) 641-2950 Ext. 24 Brightquay Lending Services, Inc. www.brightquaylending.com NMLS #318760
Industry/Entity Type
Real Estate
Look and feel
Each slider illustrates characteristics of the customer's brand and the style your logo design should communicate.

```html
<!DOCTYPE html>
<html lang="en">
<head>
<meta charset="utf-8">
<title>Hard Money Originators Wanted – Brightquay Lending Services</title>
<link rel="stylesheet" href="https://fonts.googleapis.com/css2?family=Montserrat:wght@500;600;700&display=swap">
<style>
  :root {
    --backdrop: #2a211c;
    --paper: #ffffff;
    --brand-blue: #1f66e6;
    --brand-olive: #a0a612;
    --text-light: #ffffff;
    --sky-top: #7fa6d6;
    --house-white: #d9dedf;
    --photo-warm: #c9a77f;
    --photo-site: #8c7a62;
    --photo-wood: #9a8468;
  }
  * { box-sizing: border-box; margin: 0; padding: 0; }
  html, body {
    width: 1200px; height: 935px; overflow: hidden;
    background: var(--backdrop);
    font-family: "Montserrat", sans-serif;
  }
  .flyer {
    position: absolute; left: 260px; top: 27px;
    width: 680px; height: 880px;
    background: var(--paper);
    overflow: hidden;
  }
  .photo { position: absolute; }
  .photo--house {
    left: 0; top: 0; width: 420px; height: 510px;
    background: linear-gradient(180deg, var(--sky-top) 0%, #c4d3e4 35%, var(--house-white) 60%, #a9aeb0 100%);
  }
  .photo--inspection {
    left: 0; top: 510px; width: 232px; height: 170px;
    background: linear-gradient(160deg, #e8e4dc 0%, var(--photo-warm) 100%);
  }
  .photo--worker {
    left: 232px; top: 525px; width: 228px; height: 180px;
    background: linear-gradient(160deg, #d8d2c4 0%, var(--photo-site) 100%);
  }
  .photo--carpenter {
    left: 460px; top: 565px; width: 220px; height: 150px;
    background: linear-gradient(160deg, #b9aa92 0%, var(--photo-wood) 100%);
  }
  .recruit-panel {
    position: absolute; left: 400px; top: 0;
    width: 280px; height: 565px;
    background: var(--brand-blue);
    color: var(--text-light);
    padding: 62px 22px 0 26px;
  }
  .recruit-panel__title {
    font-weight: 600; font-size: 22px; line-height: 1.25;
    letter-spacing: 1px; text-transform: uppercase;
    margin-bottom: 34px;
  }
  .benefits { list-style: none; }
  .benefits li {
    position: relative; padding-left: 26px;
    font-size: 13.5px; font-weight: 500; line-height: 1.2;
    letter-spacing: 0.5px; margin-bottom: 20px;
  }
  .benefits li svg { position: absolute; left: 0; top: 2px; }
  .nmls {
    position: absolute; left: 26px; bottom: 26px;
    font-size: 26px; font-weight: 500; letter-spacing: 1px;
  }
  .company {
    position: absolute; left: 28px; top: 765px;
    display: flex; align-items: center; gap: 12px;
    width: 250px;
  }
  .company__dot {
    flex: none; width: 34px; height: 34px; border-radius: 50%;
    background: var(--brand-blue);
  }
  .company__name {
    font-size: 15px; font-weight: 600; line-height: 1.3;
    color: var(--brand-blue);
  }
  .contact {
    position: absolute; left: 300px; top: 730px;
    width: 352px; height: 124px;
    background: var(--brand-olive);
    color: var(--text-light);
    padding: 14px 18px 0 24px;
  }
  .contact__label { font-size: 15px; font-weight: 500; letter-spacing: 1px; }
  .contact__phone { font-size: 20px; font-weight: 600; margin: 4px 0 6px; letter-spacing: 0.5px; }
  .contact__line { font-size: 12.5px; font-weight: 500; line-height: 1.45; }
</style>
</head>
<body>
  <main class="flyer">
    <div class="photo photo--house" role="img" aria-label="Photo of a large white two-storey house with garage doors under a blue sky"></div>
    <div class="photo photo--inspection" role="img" aria-label="Photo of two people reviewing plans in a home under renovation"></div>
    <div class="photo photo--worker" role="img" aria-label="Photo of a smiling construction worker in a hard hat carrying lumber"></div>
    <div class="photo photo--carpenter" role="img" aria-label="Photo of a carpenter in a hard hat cutting wood on a job site"></div>

    <section class="recruit-panel">
      <h1 class="recruit-panel__title">Hard Money<br>Originators Wanted</h1>
      <ul class="benefits">
        <li><svg width="12" height="12" viewBox="0 0 12 12"><path d="M0 0 L12 6 L0 12 Z" fill="#fff"/></svg>No Licensing Required</li>
        <li><svg width="12" height="12" viewBox="0 0 12 12"><path d="M0 0 L12 6 L0 12 Z" fill="#fff"/></svg>Work As Independent Contractor</li>
        <li><svg width="12" height="12" viewBox="0 0 12 12"><path d="M0 0 L12 6 L0 12 Z" fill="#fff"/></svg>1% Flat Finders Fee on Each Loan</li>
        <li><svg width="12" height="12" viewBox="0 0 12 12"><path d="M0 0 L12 6 L0 12 Z" fill="#fff"/></svg>Referral Compensation for Recruiting New Originators</li>
        <li><svg width="12" height="12" viewBox="0 0 12 12"><path d="M0 0 L12 6 L0 12 Z" fill="#fff"/></svg>Immediate Payouts</li>
        <li><svg width="12" height="12" viewBox="0 0 12 12"><path d="M0 0 L12 6 L0 12 Z" fill="#fff"/></svg>Programs Offered Nationwide</li>
        <li><svg width="12" height="12" viewBox="0 0 12 12"><path d="M0 0 L12 6 L0 12 Z" fill="#fff"/></svg>Marketing Assistance and Support Available</li>
      </ul>
      <p class="nmls">NMLS #318760</p>
    </section>

    <div class="company">
      <span class="company__dot"></span>
      <span class="company__name">Brightquay Lending Services, Inc.</span>
    </div>

    <section class="contact">
      <p class="contact__label">contact us :</p>
      <p class="contact__phone">(800) 641-2950 Ext. 24</p>
      <p class="contact__line">Email : mpelton@brightquaylending.com</p>
      <p class="contact__line">Web : www.brightquaylending.com</p>
    </section>
  </main>
</body>
</html>
```